Flyer Marbleknot

We need a 4-page flyer in A5 format. Font: Univers LT Std 45 Light Background color violet: 77/100/0/31 The following colors should be used for the design (text, graphic elements): White or green: 67/0/100/0 There is already a version this flyer. Flyer is attached. Flyer is attached. Please adopt style. The photos from the flyer may no longer be used.

```html
<!DOCTYPE html>
<html lang="de">
<head>
<meta charset="utf-8">
<title>Marbleknot Flyer</title>
<link rel="stylesheet" href="https://fonts.googleapis.com/css2?family=Heebo:wght@300;400;500;700&display=swap">
<style>
  :root {
    --violet: #4a1060;
    --violet-deep: #3a0a4d;
    --lavender: #ebe2ee;
    --lavender-soft: #e2d7e6;
    --paper: #ffffff;
    --stage: #eeeeee;
    --green: #2fb53a;
    --line: #c9b9cf;
    --ink: #3d3d3d;
  }
  * { box-sizing: border-box; margin: 0; padding: 0; }
  html, body { width: 1200px; height: 758px; overflow: hidden; }
  body {
    background: var(--stage);
    font-family: "Heebo", "Helvetica Neue", Arial, sans-serif;
    font-weight: 300;
    position: relative;
  }
  .spread { position: absolute; left: 69px; top: 11px; width: 1036px; height: 732px; box-shadow: 0 0 6px rgba(0,0,0,.12); }
  .page { position: absolute; top: 0; height: 732px; width: 518px; overflow: hidden; }
  .page--left { left: 0; background: var(--paper); }
  .page--right { left: 518px; background: var(--lavender); }
  .page--right::before { content: ""; position: absolute; left: 0; top: 0; bottom: 0; width: 14px; background: linear-gradient(to right, rgba(0,0,0,.08), rgba(0,0,0,0)); }

  .intro { position: absolute; left: 32px; top: 73px; width: 420px; color: var(--violet); font-size: 17px; line-height: 25px; }
  .intro strong { font-weight: 700; }
  .intro p + p { margin-top: 25px; }

  .violet-band { position: absolute; left: 0; top: 354px; width: 518px; height: 378px; background: var(--violet); }

  .article-table { position: absolute; top: 308px; width: 218px; border-collapse: collapse; background: #fff; font-size: 6px; color: #555; }
  .article-table th { background: var(--violet); color: #fff; font-weight: 500; text-align: left; padding: 0 3px; height: 13px; }
  .article-table td { border: 1px solid #cfcfcf; padding: 0 3px; height: 13px; white-space: nowrap; }
  .article-table td:first-child { width: 44px; }
  .article-table--blue { left: 32px; }
  .article-table--black { left: 268px; }

  .features { position: absolute; left: 32px; top: 460px; list-style: none; color: #fff; font-size: 12.5px; line-height: 16px; font-weight: 400; }
  .features li { position: absolute; left: 0; width: 240px; padding-left: 20px; }
  .features li svg { position: absolute; left: 0; top: 2px; }
  .features li:nth-child(1) { top: 0; }
  .features li:nth-child(2) { top: 85px; }
  .features li:nth-child(3) { top: 192px; }

  .product-visual { position: absolute; left: 323px; top: 471px; width: 141px; height: 244px; border-radius: 40px 40px 20px 20px; background: radial-gradient(ellipse at 50% 55%, #2a0a36 0%, #35103f 55%, var(--violet) 100%); }

  .callouts { position: absolute; left: 0; top: 0; }

  .title { position: absolute; left: 41px; top: 70px; color: var(--ink); font-size: 30px; font-weight: 300; letter-spacing: -0.2px; }
  .step { position: absolute; top: 142px; width: 184px; }
  .step--one { left: 41px; }
  .step--two { left: 260px; }
  .step__frame { position: relative; width: 184px; height: 242px; border: 2px solid var(--violet); background: var(--paper); }
  .step__drawing { position: absolute; inset: 0; background: linear-gradient(160deg, #faf8fb, var(--lavender-soft)); }
  .step__number { position: absolute; left: 8px; top: 8px; width: 14px; height: 14px; border-radius: 50%; background: var(--violet-deep); color: #fff; font-size: 9px; font-weight: 500; text-align: center; line-height: 14px; }
  .step__sizes { position: absolute; left: 80px; top: 165px; font-size: 11px; line-height: 13px; color: var(--ink); font-weight: 400; }
  .step__warning { position: absolute; right: 8px; top: 8px; }
  .step__text { margin-top: 14px; color: var(--ink); font-size: 16.5px; line-height: 24.4px; }
</style>
</head>
<body>
  <div class="spread">
    <section class="page page--left">
      <div class="intro">
        <p><strong>Solide, rutschfest und stabil</strong> - für maximale Mobilität. Schnell und einfach an jeder Gehhilfe zu montieren, helfen sie, trittsicher durchs Leben zu gehen.</p>
        <p>Der «Aufsatz für Gehhilfen Marbleknot» — ein cleveres Produkt SWISS MADE — wird für Gehhilfen in den gängigsten Grössen angeboten.</p>
      </div>

      <div class="violet-band"></div>

      <table class="article-table article-table--blue">
        <tr><th>Art. Nr.</th><th>Bezeichnung</th></tr>
        <tr><td>302000001</td><td>Aufsatz für Gehhilfe Marbleknot blau einzeln S</td></tr>
        <tr><td>302000002</td><td>Aufsatz für Gehhilfe Marbleknot blau einzeln M</td></tr>
        <tr><td>302000003</td><td>Aufsatz für Gehhilfe Marbleknot blau einzeln L</td></tr>
        <tr><td>302000021</td><td>Aufsatz für Gehhilfe Marbleknot blau Set à 2 Stück S</td></tr>
        <tr><td>302000022</td><td>Aufsatz für Gehhilfe Marbleknot blau Set à 2 Stück M</td></tr>
        <tr><td>302000023</td><td>Aufsatz für Gehhilfe Marbleknot blau Set à 2 Stück L</td></tr>
      </table>
      <table class="article-table article-table--black">
        <tr><th>Art. Nr.</th><th>Bezeichnung</th></tr>
        <tr><td>302000004</td><td>Aufsatz für Gehhilfe Marbleknot schwarz einzeln S</td></tr>
        <tr><td>302000005</td><td>Aufsatz für Gehhilfe Marbleknot schwarz einzeln M</td></tr>
        <tr><td>302000006</td><td>Aufsatz für Gehhilfe Marbleknot schwarz einzeln L</td></tr>
        <tr><td>302000024</td><td>Aufsatz für Gehhilfe Marbleknot schwarz Set à 2 Stück S</td></tr>
        <tr><td>302000025</td><td>Aufsatz für Gehhilfe Marbleknot schwarz Set à 2 Stück M</td></tr>
        <tr><td>302000026</td><td>Aufsatz für Gehhilfe Marbleknot schwarz Set à 2 Stück L</td></tr>
      </table>

      <div class="product-visual" role="img" aria-label="Produktansicht des dunklen Gehhilfeaufsatzes mit Klemmbride und vierfüssiger Sohle"></div>

      <svg class="callouts" width="518" height="732" viewBox="0 0 518 732" aria-hidden="true">
        <g fill="none" stroke="#fff" stroke-width="1" opacity=".85">
          <polyline points="32,485 236,485 249,473 380,473 380,489"/>
          <polyline points="32,587 231,587 242,575 442,575 442,596"/>
          <polyline points="32,663 237,663 248,652 285,652"/>
        </g>
        <g fill="#fff">
          <circle cx="380" cy="490" r="2"/>
          <circle cx="442" cy="597" r="2"/>
          <circle cx="286" cy="652" r="2"/>
        </g>
      </svg>

      <ul class="features">
        <li><svg width="13" height="13" viewBox="0 0 13 13"><circle cx="6.5" cy="6.5" r="6.5" fill="#d9d0dd"/><polyline points="3.5,6.7 5.7,8.8 9.6,4.5" fill="none" stroke="#4a1060" stroke-width="1.6"/></svg>Metallkomponenten Aus<br>Rostfreiem Stahl</li>
        <li><svg width="13" height="13" viewBox="0 0 13 13"><circle cx="6.5" cy="6.5" r="6.5" fill="#d9d0dd"/><polyline points="3.5,6.7 5.7,8.8 9.6,4.5" fill="none" stroke="#4a1060" stroke-width="1.6"/></svg>Spezielles Sohlenmaterial Für<br>Maximalen Halt Auch Auf Nassen<br>Und Rutschigen Böden</li>
        <li><svg width="13" height="13" viewBox="0 0 13 13"><circle cx="6.5" cy="6.5" r="6.5" fill="#d9d0dd"/><polyline points="3.5,6.7 5.7,8.8 9.6,4.5" fill="none" stroke="#4a1060" stroke-width="1.6"/></svg>Profil Für Mehr Halt</li>
      </ul>
    </section>

    <section class="page page--right">
      <h1 class="title">Marbleknot Gebrauchsanweisung</h1>

      <div class="step step--one">
        <div class="step__frame">
          <div class="step__drawing" role="img" aria-label="Technische Zeichnung: Schaft der Gehhilfe mit Pfeilen zur Durchmessermessung"></div>
          <span class="step__number">1</span>
          <div class="step__sizes">16-18 mm (S)<br>19-21 mm (M)<br>22-24 mm (L)</div>
        </div>
        <p class="step__text">Zur Grössenbestimmung den Schaft-Durchmesser im unteren Teil der Gehhilfe messen.</p>
      </div>

      <div class="step step--two">
        <div class="step__frame">
          <div class="step__drawing" role="img" aria-label="Technische Zeichnung: Aufsatz auf dem Krückenrohr montiert, Klemmlaschen nach hinten"></div>
          <span class="step__number">2</span>
          <svg class="step__warning" width="27" height="24" viewBox="0 0 27 24" aria-hidden="true">
            <polygon points="13.5,1 26,23 1,23" fill="#2fb53a" stroke="#1f8a28" stroke-width="1"/>
            <rect x="12.2" y="8" width="2.6" height="8" fill="#fff"/>
            <rect x="12.2" y="18" width="2.6" height="2.6" fill="#fff"/>
          </svg>
        </div>
        <p class="step__text">Den Gehhilfeaufsatz so auf das Krückenrohr stecken, dass die Klemmlaschen der Bride, in Gehrichtung betrachtet, nach hinten zeigen. Die Schraube mit dem mitgelieferten Inbusschlüssel anziehen.</p>
      </div>
    </section>
  </div>
</body>
</html>
```